Chiropractor needs a snazzy business card

Business card for a chiropractic office.
Office treats patients of all ages.
Focus is on a natural lifestyle.
Colors can include the logo colors as well as white and a little orange.
Ideally the card would have something chiropractic related such as a spine.

The back of the card should have a items for making appointments (date, times....)

```html
<!DOCTYPE html>
<html lang="en">
<head>
<meta charset="utf-8">
<title>Meridian Chiropractic – Business Card</title>
<link rel="stylesheet" href="https://fonts.googleapis.com/css2?family=Open+Sans:wght@400;600;700&display=swap">
<style>
  :root {
    --navy: #0d4a7c;
    --green: #4cb848;
    --white: #ffffff;
    --ink: #3a3a3a;
    --rule: #8a8a8a;
    --backdrop: #ebe8e3;
  }
  * { box-sizing: border-box; margin: 0; padding: 0; }
  html, body {
    width: 1200px; height: 1024px; overflow: hidden;
    background: var(--backdrop);
    font-family: "Open Sans", Arial, sans-serif;
  }
  .card {
    position: absolute; left: 320px;
    width: 560px; height: 320px;
    background: var(--white);
    overflow: hidden;
    box-shadow: 0 6px 18px rgba(0,0,0,.18);
  }
  .card--front { top: 110px; }
  .card--back { top: 594px; }

  /* front */
  .front__band {
    position: absolute; left: 0; right: 0; bottom: 0; height: 34px;
    background: var(--green);
  }
  .front__tab {
    position: absolute; right: 0; bottom: 34px; width: 178px; height: 46px;
    background: var(--navy);
    border-top-left-radius: 6px;
    color: var(--white); font-size: 12px;
    display: flex; align-items: center; justify-content: center;
  }
  .front__tab::after {
    content: ""; position: absolute; left: 0; right: 0; top: 46px; height: 34px;
    background: var(--navy);
  }
  .brand {
    color: var(--navy); font-weight: 600; line-height: 1;
    letter-spacing: 1px;
  }
  .brand__name { font-size: 40px; }
  .brand__sub { font-size: 24px; letter-spacing: 3px; margin-top: 4px; }
  .front__brand { position: absolute; left: 40px; top: 70px; }
  .front__contact { position: absolute; left: 40px; top: 168px; }
  .person { font-size: 16px; color: var(--navy); font-weight: 700; margin-bottom: 6px; }
  .person__role { color: var(--green); font-weight: 600; font-size: 13px; }
  .person__sep { color: var(--ink); font-weight: 400; margin: 0 4px; }
  .contact-line {
    display: flex; align-items: center; gap: 8px;
    font-size: 15px; color: var(--ink); line-height: 22px;
  }
  .contact-line svg { width: 12px; height: 12px; flex: none; }

  /* back */
  .back__panel {
    position: absolute; right: 0; top: 0; bottom: 0; width: 200px;
    background: var(--navy);
  }
  .back__brand {
    position: absolute; right: 16px; top: 120px; width: 330px; text-align: right;
  }
  .back__brand .brand__name { font-size: 32px; }
  .back__brand .brand__sub { font-size: 19px; color: var(--navy); }
  .back__band {
    position: absolute; left: 0; right: 0; bottom: 0; height: 30px;
    background: var(--green);
    color: var(--white); font-size: 12px;
    display: flex; align-items: center; padding-left: 40px;
  }
  .back__rule {
    position: absolute; left: 0; right: 200px; bottom: 30px; height: 4px;
    background: var(--navy);
  }
  .appointment {
    position: absolute; left: 30px; top: 28px; width: 300px;
  }
  .appointment__title {
    font-size: 15px; letter-spacing: 1px; color: var(--ink);
    margin-bottom: 4px;
  }
  .field {
    display: flex; align-items: flex-end; gap: 8px;
    font-size: 12px; color: var(--ink); height: 36px;
  }
  .field__line { flex: 1; border-bottom: 1px solid var(--rule); margin-bottom: 3px; }
  .field-row { display: flex; gap: 16px; }
  .field-row .field { flex: 1; }
</style>
</head>
<body>

<section class="card card--front" aria-label="Business card front">
  <div class="brand front__brand">
    <div class="brand__name">MERIDIAN</div>
    <div class="brand__sub">CHIROPRACTIC</div>
  </div>

  <div class="front__contact">
    <p class="person">Daniel Hart<span class="person__sep">|</span><span class="person__role">Chiropractor</span></p>
    <p class="contact-line">
      <svg viewBox="0 0 12 12"><path d="M2.5 1l2 2.2-1 1.3c.7 1.5 1.8 2.6 3.2 3.3l1.3-1 2.1 2-1.2 1.8C5 10.2 1.6 6.8 1 2.3z" fill="var(--green)"/></svg>
      000-000-000
    </p>
    <p class="contact-line">
      <svg viewBox="0 0 12 12"><rect x="3" y="1" width="6" height="10" rx="1" fill="none" stroke="var(--green)" stroke-width="1.4"/></svg>
      000-000-0000
    </p>
    <p class="contact-line">
      <svg viewBox="0 0 12 12"><rect x="1" y="2.5" width="10" height="7" fill="var(--green)"/><path d="M1 2.5l5 4 5-4" fill="none" stroke="#fff" stroke-width="1"/></svg>
      name@domainname.com
    </p>
  </div>

  <div class="front__band"></div>
  <div class="front__tab">www.webname.com</div>
</section>

<section class="card card--back" aria-label="Business card back">
  <div class="back__panel"></div>
  <div class="brand back__brand">
    <div class="brand__name" style="color:var(--white)">MERIDIAN</div>
    <div class="brand__sub" style="color:var(--white)">CHIROPRACTIC</div>
  </div>

  <div class="appointment">
    <p class="appointment__title">APPOINTMENT</p>
    <div class="field"><span>FOR:</span><span class="field__line"></span></div>
    <div class="field"><span>DAY:</span><span class="field__line"></span></div>
    <div class="field-row">
      <div class="field"><span>DATE:</span><span class="field__line"></span></div>
      <div class="field"><span>TIME:</span><span class="field__line"></span></div>
    </div>
  </div>

  <div class="back__rule"></div>
  <div class="back__band">www.websitename.com</div>
</section>

</body>
</html>
```